Insight Plus. needs Business Cards

For this project, we need business cards (currently have also put a call out for a logo). We are a start-up called Insight Plus. This is our second company (our first one was called Querivance). Traditionally we have been providing market research services across different sectors, primarily financial services and the pharmaceutical industry. However, we now want to go beyond market research to offer more (Plus.)... strategic consulting and big data knowledge management. We want our brand to be approachable, creative, fun but professional.

Target Market(s)

The target audience is a business professional - we are B2B (business to business) and do not sell our services to individuals. The brands we work with are major brands across industries, but primarily automotive, financial and pharmaceutical.

Industry/Entity Type

Market Research

Font styles to use
Serif
Sans Serif
Other font styles liked:
• Calibri

Requirements
Must have
• Be clean, simple, modern
Show our address and phone number and email address and website URL
We do not need to have titles showing.

```html
<!DOCTYPE html>
<html lang="en">
<head>
<meta charset="utf-8">
<title>Insight Plus. Business Cards</title>
<link rel="stylesheet" href="https://fonts.googleapis.com/css2?family=Open+Sans:wght@400;600;700&display=swap">
<style>
  :root {
    --page-bg: #e8eaec;
    --teal: #0cbfa3;
    --teal-light: #2ccbb1;
    --teal-dark: #03ad91;
    --teal-deep: #00a386;
    --mark-tone: #06ab8f;
    --white: #ffffff;
    --shadow: rgba(0, 0, 0, 0.18);
  }
  * { box-sizing: border-box; margin: 0; padding: 0; }
  html, body {
    width: 1200px; height: 755px; overflow: hidden;
    background: var(--page-bg);
    font-family: "Open Sans", Arial, sans-serif;
  }
  .sheet { position: relative; width: 1200px; height: 755px; }
  .card {
    position: absolute; width: 521px; height: 313px; overflow: hidden;
    background: var(--teal);
    box-shadow: 0 8px 18px var(--shadow);
  }
  .card--front.row-1 { left: 59px; top: 50px; }
  .card--back.row-1  { left: 617px; top: 50px; }
  .card--front.row-2 { left: 59px; top: 392px; }
  .card--back.row-2  { left: 617px; top: 392px; }

  .card__curves { position: absolute; inset: 0; width: 100%; height: 100%; }
  .card__glow {
    position: absolute; border-radius: 50%;
    background: radial-gradient(circle, rgba(255,255,255,0.22) 0%, rgba(255,255,255,0) 70%);
  }
  .card--front .card__glow { left: -10px; top: 70px; width: 190px; height: 150px; }
  .card--back .card__glow { left: 20px; top: -10px; width: 110px; height: 110px; }

  .card__header {
    position: absolute; left: 0; top: 0; width: 100%; height: 82px;
    background: rgba(0, 160, 132, 0.25);
  }
  .card__header-rule {
    position: absolute; left: 0; top: 82px; width: 100%; height: 5px;
    background: var(--teal-deep);
  }
  .brand-name {
    position: absolute; left: 45px; top: 26px;
    color: var(--white); font-weight: 600; font-size: 19px; letter-spacing: 0.2px;
  }
  .holder-name {
    position: absolute; left: 273px; top: 129px;
    color: var(--white); font-weight: 700; font-size: 17.5px;
  }
  .contact-list { position: absolute; left: 239px; top: 182px; list-style: none; }
  .contact-list li {
    display: flex; align-items: center; height: 20.5px;
    color: var(--white); font-weight: 700; font-size: 7.6px;
  }
  .contact-list svg { width: 14px; height: 12px; margin-right: 14px; flex: none; }
  .card__footer {
    position: absolute; left: 0; bottom: 0; width: 200px; height: 22px;
    background: var(--teal-deep);
    clip-path: polygon(0 0, 176px 0, 100% 100%, 0 100%);
  }
  .website {
    position: absolute; left: 40px; bottom: 6px;
    color: var(--white); font-size: 7.8px; font-weight: 600; letter-spacing: 2px;
  }
  .back-name {
    position: absolute; left: 0; right: 0; top: 118px; text-align: center;
    color: var(--mark-tone); font-weight: 600; font-size: 58px; letter-spacing: -1px;
  }
</style>
</head>
<body>
<main class="sheet">

  <!-- Row 1 -->
  <section class="card card--front row-1">
    <svg class="card__curves" viewBox="0 0 521 313" aria-hidden="true">
      <path d="M380 0 C300 60 190 120 170 200 C160 260 230 300 300 313 L521 313 L521 0 Z" fill="rgba(255,255,255,0.05)"/>
      <path d="M0 200 C80 190 150 230 200 313 L0 313 Z" fill="rgba(0,150,122,0.12)"/>
    </svg>
    <div class="card__glow"></div>
    <div class="card__header"></div>
    <div class="card__header-rule"></div>
    <div class="brand-name">Insight Plus.</div>
    <div class="holder-name">Your Name Here</div>
    <ul class="contact-list">
      <li><svg viewBox="0 0 14 12"><path d="M7 0.5a3.6 3.6 0 0 0-3.6 3.6C3.4 7 7 11.5 7 11.5S10.6 7 10.6 4.1A3.6 3.6 0 0 0 7 0.5Zm0 5a1.4 1.4 0 1 1 0-2.8 1.4 1.4 0 0 1 0 2.8Z" fill="#fff"/></svg>24 - 28 Harbor Lane no. 7, Brookfield, CT 06804</li>
      <li><svg viewBox="0 0 14 12"><path d="M3.5 1.2l2 2-1.2 1.3c.6 1.4 1.6 2.4 3 3l1.3-1.2 2 2-1.4 1.5C5.8 9.6 2.6 6.4 2.1 2.6Z" fill="#fff"/></svg>555 204 7168</li>
      <li><svg viewBox="0 0 14 12"><rect x="4" y="0.5" width="6" height="3" fill="#fff"/><rect x="2" y="4" width="10" height="4.5" rx="1" fill="#fff"/><rect x="4" y="7.5" width="6" height="4" fill="#fff" stroke="#0cbfa3" stroke-width="0.8"/></svg>555 204 7169</li>
      <li><svg viewBox="0 0 14 12"><rect x="2" y="2" width="10" height="8" rx="1" fill="#fff"/><path d="M2.5 2.8 7 6.3l4.5-3.5" fill="none" stroke="#0cbfa3" stroke-width="0.9"/></svg>hello@insightplus.example</li>
    </ul>
    <div class="card__footer"></div>
    <div class="website">www.insightplus.example</div>
  </section>

  <section class="card card--back row-1">
    <svg class="card__curves" viewBox="0 0 521 313" aria-hidden="true">
      <path d="M380 0 C320 80 210 120 180 200 C160 260 220 300 290 313 L521 313 L521 0 Z" fill="rgba(0,150,122,0.10)"/>
    </svg>
    <div class="card__glow"></div>
    <div class="back-name">Insight Plus.</div>
  </section>

  <!-- Row 2 -->
  <section class="card card--front row-2">
    <svg class="card__curves" viewBox="0 0 521 313" aria-hidden="true">
      <path d="M380 0 C300 60 190 120 170 200 C160 260 230 300 300 313 L521 313 L521 0 Z" fill="rgba(255,255,255,0.05)"/>
      <path d="M0 200 C80 190 150 230 200 313 L0 313 Z" fill="rgba(0,150,122,0.12)"/>
    </svg>
    <div class="card__glow"></div>
    <div class="card__header"></div>
    <div class="card__header-rule" style="background: rgba(0,163,134,0.35)"></div>
    <div class="brand-name">Insight Plus.</div>
    <div class="holder-name">Your Name Here</div>
    <ul class="contact-list">
      <li><svg viewBox="0 0 14 12"><path d="M7 0.5a3.6 3.6 0 0 0-3.6 3.6C3.4 7 7 11.5 7 11.5S10.6 7 10.6 4.1A3.6 3.6 0 0 0 7 0.5Zm0 5a1.4 1.4 0 1 1 0-2.8 1.4 1.4 0 0 1 0 2.8Z" fill="#fff"/></svg>24 - 28 Harbor Lane no. 7, Brookfield, CT 06804</li>
      <li><svg viewBox="0 0 14 12"><path d="M3.5 1.2l2 2-1.2 1.3c.6 1.4 1.6 2.4 3 3l1.3-1.2 2 2-1.4 1.5C5.8 9.6 2.6 6.4 2.1 2.6Z" fill="#fff"/></svg>555 204 7168</li>
      <li><svg viewBox="0 0 14 12"><rect x="4" y="0.5" width="6" height="3" fill="#fff"/><rect x="2" y="4" width="10" height="4.5" rx="1" fill="#fff"/><rect x="4" y="7.5" width="6" height="4" fill="#fff" stroke="#0cbfa3" stroke-width="0.8"/></svg>555 204 7169</li>
      <li><svg viewBox="0 0 14 12"><rect x="2" y="2" width="10" height="8" rx="1" fill="#fff"/><path d="M2.5 2.8 7 6.3l4.5-3.5" fill="none" stroke="#0cbfa3" stroke-width="0.9"/></svg>hello@insightplus.example</li>
    </ul>
    <div class="card__footer"></div>
    <div class="website">www.insightplus.example</div>
  </section>

  <section class="card card--back row-2">
    <svg class="card__curves" viewBox="0 0 521 313" aria-hidden="true">
      <path d="M380 0 C320 80 210 120 180 200 C160 260 220 300 290 313 L521 313 L521 0 Z" fill="rgba(0,150,122,0.10)"/>
    </svg>
    <div class="card__glow"></div>
    <div class="back-name">Insight Plus.</div>
  </section>

</main>
</body>
</html>
```